Summit Relay Business Card

Side 1: Summit Relay Logo (logo without Maltese cross) with industrial rope rescue related theme. Our company services - TRAINING - Fire Training, Confined Space Rescue Training, Rope Rescue training, Hazmat Training, Incident Command, EMS, Pump Operations Training. Website - summitrelay-example.com.
Side 2: Summit Relay Fire Department Logo (logo with Maltese cross) with Firefighter related theme. Company (division) services - FIELD SERVICES - Fire Department, Stand-by Rescue, Safety, EMS, Planning. "Supporting the Emergency Response Community Since 1967"

Add contact information wherever it makes since (Name, Email, Phone).
I would like it to represent the Summit Relay Fire Department Logo as a division not as a separate entity without saying it, possibly by depicting it in the background of Side 2 instead of being a standalone picture like the logo on Side 1.

```html
<!DOCTYPE html>
<html lang="en">
<head>
<meta charset="utf-8">
<title>Summit Relay Business Card</title>
<link rel="stylesheet" href="https://fonts.googleapis.com/css2?family=Montserrat:wght@400;500;600;700&display=swap">
<style>
  :root {
    --page-bg: #1d1d1f;
    --card-light: #58585b;
    --card-dark: #38383a;
    --accent-red: #e32228;
    --text-light: #e9e9ea;
    --text-muted: #cfcfd1;
    --divider: #bdbdc0;
  }
  * { box-sizing: border-box; margin: 0; padding: 0; }
  html, body {
    width: 1200px; height: 1200px; overflow: hidden;
    background: var(--page-bg);
    font-family: "Montserrat", sans-serif;
    color: var(--text-light);
  }
  .stage {
    width: 1200px; height: 1200px;
    display: flex; flex-direction: column; align-items: center; justify-content: center;
    gap: 56px;
  }
  .card {
    position: relative;
    width: 860px; height: 491px;
    background: radial-gradient(ellipse at 55% 45%, var(--card-light) 0%, var(--card-dark) 75%);
    box-shadow: 0 10px 30px rgba(0,0,0,.55);
    overflow: hidden;
  }

  /* Field services side */
  .brand-mark {
    position: absolute; left: 450px; top: 120px;
    display: flex; align-items: center; gap: 14px;
  }
  .brand-mark .dot {
    width: 52px; height: 52px; border-radius: 50%;
    border: 3px solid var(--accent-red);
  }
  .brand-mark .name {
    font-size: 30px; font-weight: 600; letter-spacing: 4px;
    color: var(--text-muted); text-transform: uppercase;
  }
  .brand-rule {
    position: absolute; left: 450px; top: 196px; width: 330px; height: 2px;
    background: var(--accent-red);
  }
  .service-list { list-style: none; position: absolute; font-size: 21px; line-height: 31px; }
  .service-list li::before {
    content: ""; display: inline-block; width: 7px; height: 7px; border-radius: 50%;
    background: var(--accent-red); vertical-align: middle; margin-right: 10px;
  }
  .service-list.left { left: 64px; top: 128px; }
  .service-list.right { right: 64px; top: 330px; text-align: right; }
  .service-list.right li::before { display: none; }
  .service-list.right li::after {
    content: ""; display: inline-block; width: 7px; height: 7px; border-radius: 50%;
    background: var(--accent-red); vertical-align: middle; margin-left: 12px;
  }
  .tagline {
    position: absolute; left: 64px; top: 240px;
    font-size: 22px; letter-spacing: .3px;
  }

  /* Contact side */
  .person { position: absolute; left: 90px; top: 110px; }
  .person .full-name { font-size: 38px; font-weight: 700; color: var(--accent-red); }
  .person .role { font-size: 22px; color: var(--text-muted); margin-top: 4px; }
  .divider {
    position: absolute; left: 390px; top: 112px; width: 2px; height: 100px;
    background: var(--divider);
  }
  .contact-list { list-style: none; position: absolute; left: 414px; top: 112px; font-size: 20px; line-height: 34px; }
  .contact-list li { display: flex; align-items: center; gap: 10px; white-space: nowrap; }
  .contact-list svg { width: 18px; height: 18px; fill: var(--accent-red); flex: none; }
  .address { position: absolute; left: 90px; top: 250px; font-size: 21px; }
  .side-mark {
    position: absolute; right: 56px; top: 262px;
    display: flex; align-items: center; gap: 10px;
  }
  .side-mark .square { width: 26px; height: 26px; background: var(--accent-red); }
  .side-mark .name { font-size: 20px; font-weight: 600; color: var(--text-light); }
  .training { position: absolute; left: 48px; top: 350px; right: 40px; font-size: 18px; line-height: 30px; }
  .training .label { color: var(--accent-red); text-transform: uppercase; }
</style>
</head>
<body>
<main class="stage">

  <section class="card card--field-services">
    <div class="brand-mark">
      <span class="dot"></span>
      <span class="name">Summit Relay</span>
    </div>
    <div class="brand-rule"></div>
    <ul class="service-list left">
      <li>Fire Department</li>
      <li>Stand-by Rescue</li>
      <li>Safety</li>
    </ul>
    <p class="tagline">Supporting the Emergency Response Community Since 1967</p>
    <ul class="service-list right">
      <li>EMS</li>
      <li>Planning</li>
    </ul>
  </section>

  <section class="card card--contact">
    <div class="person">
      <p class="full-name">Dalton Reyes</p>
      <p class="role">Founder &amp; Director</p>
    </div>
    <div class="divider"></div>
    <ul class="contact-list">
      <li>
        <svg viewBox="0 0 24 24" aria-hidden="true"><path d="M6.6 10.8a15 15 0 0 0 6.6 6.6l2.2-2.2a1 1 0 0 1 1-.25 11.4 11.4 0 0 0 3.6.57 1 1 0 0 1 1 1V20a1 1 0 0 1-1 1A17 17 0 0 1 3 4a1 1 0 0 1 1-1h3.5a1 1 0 0 1 1 1c0 1.25.2 2.45.57 3.57a1 1 0 0 1-.25 1z"/></svg>
        (555) 218-0463
      </li>
      <li>
        <svg viewBox="0 0 24 24" aria-hidden="true"><path d="M2 5h20v14H2z M2 5l10 8 10-8" fill="none" stroke="#e32228" stroke-width="2"/></svg>
        reyes@summitrelay-example.com
      </li>
      <li>
        <svg viewBox="0 0 24 24" aria-hidden="true"><circle cx="12" cy="12" r="9" fill="none" stroke="#e32228" stroke-width="2"/><path d="M3 12h18M12 3c3 3 3 15 0 18M12 3c-3 3-3 15 0 18" fill="none" stroke="#e32228" stroke-width="1.6"/></svg>
        www.summitrelay-example.com
      </li>
    </ul>
    <p class="address">410 Harbor Lane Eastport, TX 77500</p>
    <div class="side-mark">
      <span class="square"></span>
      <span class="name">Summit Relay</span>
    </div>
    <p class="training">
      <span class="label">Training</span> - Fire Training | Confined Space Rescue Training | Rope Rescue Training |<br>
      Hazmat Training | Incident Command | EMS | Pump Operations Training
    </p>
  </section>

</main>
</body>
</html>
```